Health Coach needs a Business Card Design

Need a really modern feminine business card design for a health and lifestyle coach. Needs to use geometric shapes, muted grey/blue/green pastels and black and white - see mood board attached and logo. The client likes black and white, modern, san serif with the use of lines and possibly a shadow leaf as in the mood board. Possibly put the tag line on the back or an icon of the logo. Logo is also attached. An icon of the logo would be great too.

Target Market(s)

Women (some men) aged 30 to 50.

Industry/Entity Type

Business

Contact Information for Business Card

Marla Teveny
e-mail: hello@marlatwell.example
website: marlatwell.example
Phone: +610497258316

The tag line is "A balanced body for Life"

Font styles to use
Sans Serif

Colors
ecf7fb
cfeae6
000000
ffffff
f5f5f5

Requirements
Must have
• Black and white, logo, tag line and details
Nice to have
• Would be nice to incorporate the shadow palm.fern leaves as in the mood board and or geometric lines/shapes - see mood board. Could be either standard rectangle or would be happy with square too.
Should not have
• Flowers or decorations

```html
<!DOCTYPE html>
<html lang="en">
<head>
<meta charset="utf-8">
<title>Marla Teveny – Business Card</title>
<link rel="stylesheet" href="https://fonts.googleapis.com/css2?family=Mako&family=Montserrat:wght@400;500&display=swap">
<style>
  :root {
    --canvas: #ebecee;
    --mint: #cfe9e4;
    --mist: #d4d5d7;
    --ink-grey: #5d6262;
    --frame-grey: #6b6e6e;
    --card-black: #050709;
    --white: #ffffff;
  }
  * { margin: 0; padding: 0; box-sizing: border-box; }
  html, body {
    width: 1200px;
    height: 1000px;
    overflow: hidden;
    background: var(--canvas);
  }
  .canvas { position: relative; width: 1200px; height: 1000px; }
  .card {
    position: absolute;
    width: 372px;
    height: 372px;
    box-shadow: 1px 2px 3px rgba(0, 0, 0, 0.22);
  }
  .card-front {
    left: 206px;
    top: 311px;
    background: linear-gradient(to bottom, var(--mint) 0%, var(--mist) 100%);
    font-family: "Mako", sans-serif;
    color: var(--ink-grey);
    text-align: center;
  }
  .name-frame {
    position: absolute;
    left: 64px;
    top: 75px;
    width: 243px;
    height: 74px;
    border: 1px solid var(--frame-grey);
    display: flex;
    align-items: center;
    justify-content: center;
  }
  .name { font-size: 27px; font-weight: 400; letter-spacing: 0.2px; }
  .contact { position: absolute; left: 0; width: 100%; font-size: 17.5px; line-height: 23px; }
  .contact-phone { top: 201px; }
  .contact-web { top: 252px; }
  .card-back {
    left: 651px;
    top: 312px;
    background: var(--card-black);
    color: var(--white);
    font-family: "Montserrat", sans-serif;
    text-align: center;
  }
  .tagline {
    position: absolute;
    left: 0;
    width: 100%;
    top: 177px;
    font-size: 13px;
    font-weight: 500;
    letter-spacing: 4.2px;
    text-transform: uppercase;
  }
  .brand-name {
    position: absolute;
    left: 0;
    width: 100%;
    top: 220px;
    font-size: 18px;
    font-weight: 400;
    letter-spacing: 1px;
  }
</style>
</head>
<body>
  <main class="canvas">
    <section class="card card-front" aria-label="Card front">
      <div class="name-frame"><h1 class="name">Marla Teveny</h1></div>
      <p class="contact contact-phone">+61 049 725 8316</p>
      <p class="contact contact-web">hello@marlatwell.example<br>www. marlatwell.example</p>
    </section>
    <section class="card card-back" aria-label="Card back">
      <p class="tagline">A balanced body for life</p>
      <p class="brand-name">Marla T</p>
    </section>
  </main>
</body>
</html>
```